Sales Brochure- Generic Line Card 215mm x 140mm

Design a double-sided brochure similar to the attached sample. Cover Page contains a logo and theme that never changes. However, the background picture and the description text on the lower corner will be changed to advertise multiple services. Reverse-side contains Detailed Descriptive text related to the picture on Cover Page as well as Logo and Contact information for the business. Use the Ridgeline Controls website www.ridgelinecontrols.ca for theme, color and contact information. Also, use attached business card design for theme to match. Use the supplied logo. SIZE 215mm x 140mm

Font styles to use
Sans Serif

Colors

Designer to choose colors to be used in the design.

Requirements
Must have
• Look Similar to Sample Brochure but include Ridgeline Controls theme and colors

```html
<!DOCTYPE html>
<html lang="en">
<head>
<meta charset="utf-8">
<title>Ridgeline Controls – Line Card</title>
<link rel="stylesheet" href="https://fonts.googleapis.com/css2?family=Open+Sans:wght@300;400;600;700;800&display=swap">
<style>
  :root{
    --stage:#a7a3a5;
    --teal:#0d6e7c;
    --ink:#111214;
    --paper:#e7e7e8;
    --body:#2b2b2b;
    --orange:#f05a24;
    --white:#ffffff;
    --photo-dark:#2a2420;
    --photo-mid:#5b4a3b;
  }
  *{box-sizing:border-box;margin:0;padding:0}
  html,body{width:900px;height:1200px;overflow:hidden}
  body{background:var(--stage);font-family:"Open Sans",Arial,sans-serif;position:relative;color:var(--body)}

  .card{position:absolute;left:77px;width:741px;overflow:hidden}
  .card--front{top:46px;height:524px;background:var(--ink)}
  .card--back{top:630px;height:523px;background:var(--paper)}

  /* front */
  .cover-photo{position:absolute;left:0;top:0;width:741px;height:409px;
    background:radial-gradient(ellipse at 30% 60%,#6e6a78 0%,transparent 30%),
               radial-gradient(ellipse at 70% 45%,#7a6450 0%,transparent 45%),
               linear-gradient(135deg,var(--photo-mid),var(--photo-dark));}
  .cover-title{position:absolute;right:16px;top:16px;text-align:right;color:var(--white);line-height:1}
  .cover-title__main{display:block;font-weight:800;font-size:43px;letter-spacing:.5px}
  .cover-title__sub{display:block;font-weight:300;font-size:29.5px;margin-top:2px}
  .brand-pill{position:absolute;left:464px;top:351px;width:277px;height:58px;background:var(--white);
    border-radius:16px 0 0 0;display:flex;align-items:center;padding-left:20px;gap:10px}
  .brand-pill__mark{width:30px;height:30px;background:var(--teal);flex:none}
  .brand-name{font-weight:800;color:var(--ink);font-size:17px;letter-spacing:.5px;text-transform:uppercase;white-space:nowrap}
  .service-band{position:absolute;left:0;top:409px;width:741px;height:77px;background:var(--teal);color:var(--white);text-align:center;padding:14px 20px 0}
  .service-band__title{font-weight:700;font-size:17px;letter-spacing:.2px}
  .service-band__text{font-size:9.3px;line-height:1.4;margin-top:6px}
  .contact-bar{position:absolute;left:0;bottom:0;width:741px;height:38px;background:var(--ink);color:var(--white);
    display:flex;align-items:center;font-size:14px}
  .contact-bar__item{display:flex;align-items:center;gap:8px;white-space:nowrap}
  .contact-bar__rule{width:1px;height:22px;background:#cfcfcf}
  .contact-bar--front{justify-content:space-between;padding:0 19px 0 26px}
  .icon{width:14px;height:14px;flex:none}

  /* back */
  .back-bg{position:absolute;inset:0}
  .section{position:absolute;left:26px;width:690px}
  .section__title{color:var(--teal);font-weight:700;font-size:18.5px;letter-spacing:.1px}
  .section__text{font-size:8.6px;line-height:1.4;margin-top:6px;color:var(--body)}
  .section__sub{color:var(--teal);font-weight:700;font-size:15px;margin-top:10px}
  .feature-list{position:absolute;list-style:none;font-size:8.5px;line-height:1.3;color:var(--body)}
  .feature-list::before{content:"";position:absolute;left:2px;top:4px;bottom:8px;width:1px;background:#b9b9b9}
  .feature-list li{position:relative;padding-left:11px}
  .feature-list li::before{content:"";position:absolute;left:0;top:3px;width:5px;height:5px;border-radius:50%;background:var(--orange)}
  .tile{position:absolute;background:linear-gradient(135deg,#8a8f95,#2f3338)}
  .tile--brass{background:linear-gradient(135deg,#e2b95a,#8a5d1d)}
  .tile__label{position:absolute;left:0;right:0;bottom:0;height:20px;background:var(--orange);color:var(--white);
    font-size:10px;text-align:center;line-height:20px}

  .footer{position:absolute;left:0;bottom:0;width:741px;height:51px;background:var(--ink);color:var(--white);font-size:13px}
  .footer > *{position:absolute;top:50%;transform:translateY(-50%)}
  .footer .brand-pill{left:15px;width:144px;height:30px;border-radius:14px;padding:0 0 0 10px;gap:6px}
  .footer .brand-pill__mark{width:14px;height:14px}
  .footer .brand-name{font-size:10px;letter-spacing:0}
  .footer__phone{left:172px}
  .footer__rule--one{left:293px}
  .footer__email{left:306px}
  .footer__rule--two{left:518px}
  .footer__web{left:530px}
</style>
</head>
<body>

<section class="card card--front">
  <div class="cover-photo" role="img" aria-label="Welder in protective mask working on a large steel pipe flange in a workshop, sparks flying"></div>
  <h1 class="cover-title">
    <span class="cover-title__main">PIONEERING</span>
    <span class="cover-title__sub">RESPONSIVE MACHINING</span>
  </h1>
  <div class="brand-pill"><span class="brand-pill__mark"></span><span class="brand-name">Ridgeline Controls</span></div>
  <div class="service-band">
    <h2 class="service-band__title">COMPUTER NUMERIC CONTROL (CNC)</h2>
    <p class="service-band__text">CNC machining offers the most efficient method of producing steel and plastic components. The CNC is programmed using computer code to generate a digital machining process that can be repeated and precisely controlled. Repetitive tasks such as drilling, threading, &amp; tapping are made simple using this technology.</p>
  </div>
  <div class="contact-bar contact-bar--front">
    <span class="contact-bar__item">
      <svg class="icon" viewBox="0 0 14 14"><circle cx="7" cy="7" r="7" fill="#fff"/><path d="M4.3 3.6l1.4-.3.8 1.8-.9.7c.5 1 1.2 1.7 2.2 2.2l.7-.9 1.8.8-.3 1.4c-3.2.2-6-2.5-5.7-5.7z" fill="#111214"/></svg>780 555 0142</span>
    <span class="contact-bar__rule"></span>
    <span class="contact-bar__item">
      <svg class="icon" viewBox="0 0 14 14"><circle cx="7" cy="7" r="7" fill="#fff"/><rect x="3.5" y="4.5" width="7" height="5" fill="none" stroke="#111214"/><path d="M3.5 4.5l3.5 3 3.5-3" fill="none" stroke="#111214"/></svg>info@ridgelinecontrols.ca</span>
    <span class="contact-bar__rule"></span>
    <span class="contact-bar__item">
      <svg class="icon" viewBox="0 0 14 14"><circle cx="7" cy="7" r="7" fill="#fff"/><circle cx="7" cy="7" r="4" fill="none" stroke="#111214"/><path d="M3 7h8M7 3c-2 2-2 6 0 8M7 3c2 2 2 6 0 8" fill="none" stroke="#111214" stroke-width=".8"/></svg>www.ridgelinecontrols.ca</span>
  </div>
</section>

<section class="card card--back">
  <svg class="back-bg" width="741" height="523" viewBox="0 0 741 523" aria-hidden="true">
    <polygon points="420,0 741,0 741,260" fill="#efeff0"/>
    <polygon points="0,300 260,523 0,523" fill="#dedfe0"/>
  </svg>

  <div class="section" style="top:28px">
    <h2 class="section__title">COMPUTER NUMERIC CONTROL (CNC)</h2>
    <p class="section__text">Swiss machining (also known as “screw machining”) is the most effective way to produce small parts like pins, screws, nuts, washers and high volume parts. The Swiss machine utilizes a simultaneous machining method where multiple cutting processes occur at the same time. By simultaneously machining different features of a small part the process is dramatically quicker than CNC.</p>
    <h3 class="section__sub">Automation</h3>
  </div>
  <ul class="feature-list" style="left:26px;top:125px;width:170px">
    <li style="margin-bottom:8px">Swiss Machines up to 32mm (1.26”) Dia</li>
    <li style="margin-bottom:7px">Swiss Multi-Axis up to 8 Simultaneous Processes</li>
    <li style="margin-bottom:15px">Custom Screws, Bolts, Pins &amp; Fittings</li>
    <li style="margin-bottom:7px">Cosmetic Fasteners &amp; Glass Mounting Hardware</li>
    <li>Swiss CAD/CAM Design &amp; Programming</li>
  </ul>
  <ul class="feature-list" style="left:238px;top:125px;width:140px">
    <li style="margin-bottom:8px">“Lights-out” Production</li>
    <li style="margin-bottom:7px">High Volume Production &amp; Inventory Consignment</li>
    <li style="margin-bottom:7px">Shear Screws &amp; Shear Tension Strength Testing</li>
    <li>Equipment &amp; Machinery Fittings</li>
  </ul>
  <div class="tile" style="left:386px;top:123px;width:79px;height:92px" role="img" aria-label="Five-axis machining head cutting a part"><span class="tile__label">5-AXIS</span></div>
  <div class="tile" style="left:471px;top:123px;width:79px;height:92px" role="img" aria-label="Milling cutter close-up"><span class="tile__label">Milling</span></div>
  <div class="tile" style="left:556px;top:123px;width:79px;height:92px" role="img" aria-label="Lathe turning a metal bar"><span class="tile__label">Lathe/Turning</span></div>
  <div class="tile" style="left:641px;top:123px;width:79px;height:92px" role="img" aria-label="Swiss-type machine tooling"><span class="tile__label">SWISS</span></div>

  <div class="section" style="top:265px">
    <h2 class="section__title">SWISS SCREW &amp; SMALL PARTS</h2>
    <p class="section__text">Swiss machining (also known as “screw machining”) is the most effective way to produce small parts like pins, screws, nuts, washers and high volume parts. The Swiss machine utilizes a simultaneous machining method where multiple cutting processes occur at the same time. By simultaneously machining different features of a small part the process is dramatically quicker than CNC.</p>
  </div>
  <ul class="feature-list" style="left:26px;top:339px;width:160px">
    <li style="margin-bottom:8px">Lathe &amp; Turning Centers up to 36” Dia</li>
    <li style="margin-bottom:7px">Complex Multi-Axis Machining up to 8-Axis</li>
    <li style="margin-bottom:8px">Deep Hole Drilling/Trepanning</li>
    <li style="margin-bottom:8px">CNC Laser &amp; Cladding</li>
    <li style="margin-bottom:8px">Large Capacity Band Saw Cutting</li>
    <li>3D Surfacing &amp; Mold Machining</li>
  </ul>
  <ul class="feature-list" style="left:238px;top:339px;width:180px">
    <li style="margin-bottom:8px">Mill &amp; Machining Centers up to 120” L</li>
    <li style="margin-bottom:18px">Swiss Screw Machining</li>
    <li style="margin-bottom:8px">CNC Honing &amp; Grinding</li>
    <li style="margin-bottom:8px">Oil Field &amp; Custom Threading</li>
    <li style="margin-bottom:8px">CNC Plasma &amp; Water Jet</li>
    <li>CNC Press</li>
  </ul>
  <div class="tile" style="left:546px;top:345px;width:82px;height:96px" role="img" aria-label="Swiss CNC machine producing small turned parts"><span class="tile__label">SWISS CNC</span></div>
  <div class="tile tile--brass" style="left:636px;top:345px;width:82px;height:96px" role="img" aria-label="Pile of brass machined screws"><span class="tile__label">SCREWS</span></div>

  <div class="footer">
    <div class="brand-pill"><span class="brand-pill__mark"></span><span class="brand-name">RIDGELINE CONTROLS</span></div>
    <span class="contact-bar__item footer__phone">
      <svg class="icon" viewBox="0 0 14 14"><circle cx="7" cy="7" r="7" fill="#fff"/><path d="M4.3 3.6l1.4-.3.8 1.8-.9.7c.5 1 1.2 1.7 2.2 2.2l.7-.9 1.8.8-.3 1.4c-3.2.2-6-2.5-5.7-5.7z" fill="#111214"/></svg>780 555 0142</span>
    <span class="contact-bar__rule footer__rule--one"></span>
    <span class="contact-bar__item footer__email">
      <svg class="icon" viewBox="0 0 14 14"><circle cx="7" cy="7" r="7" fill="#fff"/><rect x="3.5" y="4.5" width="7" height="5" fill="none" stroke="#111214"/><path d="M3.5 4.5l3.5 3 3.5-3" fill="none" stroke="#111214"/></svg>info@ridgelinecontrols.ca</span>
    <span class="contact-bar__rule footer__rule--two"></span>
    <span class="contact-bar__item footer__web">
      <svg class="icon" viewBox="0 0 14 14"><circle cx="7" cy="7" r="7" fill="#fff"/><circle cx="7" cy="7" r="4" fill="none" stroke="#111214"/><path d="M3 7h8M7 3c-2 2-2 6 0 8M7 3c2 2 2 6 0 8" fill="none" stroke="#111214" stroke-width=".8"/></svg>www.ridgelinecontrols.ca</span>
  </div>
</section>

</body>
</html>
```